RT Advisory - Web Design Upgrade

We have recently designed a website (http://www.rtadvisory-example.com.au) which requires more creative and professional inputs. The website was designed using 'bright hosting site builder template' and it is currently available for viewing on the internet. Also, you are able to access the PDF files for the 6 main pages (i.e. Home, About, Services, Contaminated Land Management, Groundwater Management and Contact).

The current website has 17 pages, however, your design may only be required for the 6 main pages.

Currently the website background is white but we are open to other colours provided the company logo is adjusted accordingly.

The idea is to upgrade the existing design and, if possible, continue using 'bright hosting' as the preferred web host. So we are not sure if the design should be coded or uncoded...we leave it to your proficiency and advice.

Target Market(s)

Government organisations, landowners and developers, waste and utilities companies, community organisations and individuals.

Font styles to use
Sans Serif

Colors
0355a3
3176b5
9ccb3b
acd037
ffffff

Requirements
Nice to have
• Sliding images

```html
<!DOCTYPE html>
<html lang="en">
<head>
<meta charset="utf-8">
<title>RT Advisory — Environmental Consulting</title>
<link rel="stylesheet" href="https://fonts.googleapis.com/css2?family=Oswald:wght@300;400&family=Didact+Gothic&display=swap">
<style>
:root{
  --blue:#0355a3;
  --blue-light:#3176b5;
  --green:#9ccb3b;
  --green-2:#acd037;
  --white:#ffffff;
  --ink:#222222;
  --text:#6b6b6b;
  --footer:#363636;
  --footer-deep:#2a2a2a;
  --field:#474747;
  --rule:#555555;
}
*{box-sizing:border-box;margin:0;padding:0}
html,body{width:842px;height:1200px;overflow:hidden;background:var(--white)}
body{position:relative;font-family:"Didact Gothic",sans-serif;color:var(--text)}
.abs{position:absolute}

/* Hero slider */
.hero{left:0;top:0;width:842px;height:307px;
  background:linear-gradient(180deg,#3e64a8 0%,#35589a 55%,#2d4b82 100%)}
.hero-photo{left:0;top:0;width:842px;height:307px;
  background:radial-gradient(ellipse at 70% 45%,rgba(120,150,110,.35),transparent 60%),
             radial-gradient(ellipse at 20% 70%,rgba(150,90,110,.25),transparent 55%)}
.brand{left:80px;top:10px;display:flex;align-items:center;gap:6px;color:var(--white);font-size:12px}
.brand-mark{width:40px;height:40px;border-radius:50%;border:2px solid var(--white)}
.nav{right:87px;top:17px;display:flex;gap:6px;font-size:9px;color:var(--white)}
.hero-title{left:0;width:842px;top:122px;text-align:center;color:var(--white);
  font-family:"Oswald",sans-serif;font-weight:400;font-size:24px;letter-spacing:-.4px;line-height:30px}
.hero-sub{left:0;width:842px;top:157px;text-align:center;color:var(--white);font-size:9.5px}
.hero-btn{left:366px;top:179px;width:110px;height:35px;border:2px solid var(--white);border-radius:3px;
  color:var(--white);font-family:"Oswald",sans-serif;font-size:15px;display:flex;align-items:center;justify-content:center}
.slider-arrow{top:122px}
.dots{left:409px;top:270px;display:flex;gap:2px}
.dots i{width:7px;height:7px;border:1px solid var(--white);display:block}

/* Services */
.section-title{left:0;width:842px;top:332px;text-align:center;font-family:"Oswald",sans-serif;
  font-weight:400;font-size:18px;color:var(--ink)}
.section-title b{font-weight:400;color:var(--blue)}
.divider{left:392px;top:363px}
.section-intro{left:0;width:842px;top:381px;text-align:center;font-size:9.3px;line-height:15px}

.card-media{top:442px;width:335px;height:131px}
.media-drill{left:78px;background:linear-gradient(180deg,#5f8fc4 0%,#7d9b6a 50%,#c9b27a 100%)}
.media-wetland{left:430px;background:linear-gradient(180deg,#2f3540 0%,#7f868c 45%,#9fb3b8 65%,#6f9a3f 100%)}
.card-title{top:576px;font-family:"Oswald",sans-serif;font-weight:300;font-size:20px;color:var(--green)}
.card-text{top:605px;width:335px;font-size:8.6px;line-height:12.7px;text-align:justify}

.about-media{left:78px;top:721px;width:213px;height:167px;
  background:linear-gradient(180deg,#2f62b8 0%,#5f8fd0 50%,#8aa04a 75%,#b7a56b 100%)}
.about-title{left:306px;top:717px;font-family:"Oswald",sans-serif;font-weight:300;font-size:17px;color:#8cb52e}
.about-text{left:306px;width:458px;font-size:8.6px;line-height:12.8px;text-align:justify}
.read-more{left:699px;top:870px;width:54px;height:18px;background:var(--green);color:var(--white);
  font-family:"Oswald",sans-serif;font-size:9px;display:flex;align-items:center;justify-content:center}

/* Footer */
.footer-line{left:0;top:910px;width:842px;height:3px;background:var(--green)}
.footer{left:0;top:913px;width:842px;height:246px;background:var(--footer)}
.footer-title{font-size:15px;font-weight:400;color:#e4e4e4}
.social{left:78px;width:126px;height:20px;display:flex;align-items:center;gap:5px;padding-left:6px;
  color:var(--white);font-size:9px}
.social i{width:12px;height:12px;border-radius:50%;background:var(--white);display:block}
.s1{background:#3b5998}.s2{background:#1da1f2}.s3{background:#dd4b39}.s4{background:#8a5a4a}.s5{background:#e5393a}
.hours{left:257px;top:972px;width:141px}
.hours li{list-style:none;height:19.4px;border-bottom:1px solid var(--rule);display:flex;align-items:center;
  gap:7px;padding-left:5px;font-size:9.5px;color:#e0e0e0}
.help{left:448px;top:976px;font-size:9.5px;color:#e0e0e0;line-height:19.4px;list-style:none}
.field{left:607px;width:150px;height:17px;background:var(--field);font-size:8.5px;color:#666;padding:3px 5px}
.send{left:607px;top:1118px;width:30px;height:18px;background:var(--field);color:#e0e0e0;font-size:9.5px;
  display:flex;align-items:center;justify-content:center}
.bottom-bar{left:0;top:1159px;width:842px;height:41px;background:var(--footer-deep)}
.copyright{left:83px;top:1173px;font-size:8.5px;color:var(--white)}
</style>
</head>
<body>

<header>
  <div class="abs hero" role="img" aria-label="Slide photo of field workers in hard hats sampling groundwater beside traffic cones, tinted blue"></div>
  <div class="abs hero-photo"></div>
  <div class="abs brand"><span class="brand-mark"></span><span>RT Advisory</span></div>
  <nav class="abs nav"><span>Home</span><span>|</span><span>About Us</span><span>|</span><span>Our Services</span><span>|</span><span>Contact Us</span></nav>
  <svg class="abs slider-arrow" style="left:80px" width="22" height="44" viewBox="0 0 22 44"><polyline points="21,1 1,22 21,43" fill="none" stroke="#fff" stroke-width="1.2"/></svg>
  <svg class="abs slider-arrow" style="left:736px" width="22" height="44" viewBox="0 0 22 44"><polyline points="1,1 21,22 1,43" fill="none" stroke="#fff" stroke-width="1.2"/></svg>
  <h1 class="abs hero-title">“WE ARE A COMPANY OFFERING ENVIRONMENTAL”</h1>
  <p class="abs hero-sub">Services to clients in the private and government sectors throughout Australia</p>
  <div class="abs hero-btn">LEARN MORE</div>
  <div class="abs dots"><i></i><i></i><i></i></div>
</header>

<main>
  <h2 class="abs section-title">OUR <b>SERVICES</b></h2>
  <svg class="abs divider" width="58" height="10" viewBox="0 0 58 10"><line x1="0" y1="5" x2="25" y2="5" stroke="#555" stroke-width="1"/><circle cx="29" cy="5" r="3.2" fill="#fff" stroke="#555"/><line x1="33" y1="5" x2="58" y2="5" stroke="#555" stroke-width="1"/></svg>
  <p class="abs section-intro">We implement technical leadership in our approach, promote excellence in<br>our services and support practical solutions</p>

  <div class="abs card-media media-drill" role="img" aria-label="Photo of a yellow drilling rig and crew on a contaminated land site"></div>
  <h3 class="abs card-title" style="left:77px">Contaminated Land Management</h3>
  <p class="abs card-text" style="left:78px">Lorem Ipsum is simply dummy text of the printing and typesetting industry. Lorem Ipsum has been the industry's standard dummy text ever since the 1500s, when an unknown printer took a galley of type and scrambled it to make a type specimen book. It has survived not only five centuries, but also the leap into electronic typesetting, remaining essentially unchanged. It was popularised in the 1960s with the release of Letterfold sheets containing Lorem Ipsum passages, and more recently with desktop publishing software like Folio PageBuilder including versions of Lorem Ipsum.</p>

  <div class="abs card-media media-wetland" role="img" aria-label="Photo of a wetland at sunset under a cloudy sky"></div>
  <h3 class="abs card-title" style="left:428px">Groundwater Management</h3>
  <p class="abs card-text" style="left:429px">Lorem Ipsum is simply dummy text of the printing and typesetting industry. Lorem Ipsum has been the industry's standard dummy text ever since the 1500s, when an unknown printer took a galley of type and scrambled it to make a type specimen book. It has survived not only five centuries, but also the leap into electronic typesetting, remaining essentially unchanged. It was popularised in the 1960s with the release of Letterfold sheets containing Lorem Ipsum passages, and more recently with desktop publishing software like Folio PageBuilder including versions of Lorem Ipsum.</p>

  <div class="abs about-media" role="img" aria-label="Photo of two consultants reviewing a plan in a grassy field under a blue sky"></div>
  <h3 class="abs about-title">About RT Advisory</h3>
  <p class="abs about-text" style="top:743px">River &amp; Terrain Advisory Pty Ltd (RT Advisory) is one of the forthcoming leading environmental consultancies operating in Australia. Our clients include national, regional and local government, landowners and developers, waste and utilities companies, community organisations and individuals. The vast majority of our work comprises repeat business from existing clients and new commissions from personal recommendations.</p>
  <p class="abs about-text" style="top:806px">RT Advisory's approach combines structured thinking and an awareness of the wider picture. It is based on working in partnership with clients in order to gain a clear understanding of their needs, provision of options and on-going client liaison. Our overall aim is to meet, and where possible, surpass client's objectives, whilst fulfilling the requirements of sustainable development.</p>
  <div class="abs read-more">READ MORE</div>
</main>

<footer>
  <div class="abs footer-line"></div>
  <div class="abs footer"></div>

  <h4 class="abs footer-title" style="left:78px;top:942px">Social Connection</h4>
  <div class="abs social s1" style="top:974px"><i></i>Follow us on Circlebook</div>
  <div class="abs social s2" style="top:1000px"><i></i>Follow us on Chirper</div>
  <div class="abs social s3" style="top:1026px"><i></i>Follow us on Groupsphere</div>
  <div class="abs social s4" style="top:1053px"><i></i>Follow us on Snapgram</div>
  <div class="abs social s5" style="top:1079px"><i></i>Watch us on Viewtube</div>

  <h4 class="abs footer-title" style="left:262px;top:944px">Working Hours</h4>
  <ul class="abs hours">
    <li><svg width="9" height="9" viewBox="0 0 10 10"><circle cx="5" cy="5" r="4" fill="none" stroke="#777"/><path d="M5 2.5V5h2" fill="none" stroke="#777"/></svg>Monday: 9 AM to 6 P.M</li>
    <li><svg width="9" height="9" viewBox="0 0 10 10"><circle cx="5" cy="5" r="4" fill="none" stroke="#777"/><path d="M5 2.5V5h2" fill="none" stroke="#777"/></svg>Tuesday: 9 AM to 6 P.M</li>
    <li><svg width="9" height="9" viewBox="0 0 10 10"><circle cx="5" cy="5" r="4" fill="none" stroke="#777"/><path d="M5 2.5V5h2" fill="none" stroke="#777"/></svg>Wednesday: 9 AM to 6 P.M</li>
    <li><svg width="9" height="9" viewBox="0 0 10 10"><circle cx="5" cy="5" r="4" fill="none" stroke="#777"/><path d="M5 2.5V5h2" fill="none" stroke="#777"/></svg>Thursday: 9 AM to 6 P.M</li>
    <li><svg width="9" height="9" viewBox="0 0 10 10"><circle cx="5" cy="5" r="4" fill="none" stroke="#777"/><path d="M5 2.5V5h2" fill="none" stroke="#777"/></svg>Friday: 9 AM to 6 P.M</li>
    <li><svg width="9" height="9" viewBox="0 0 10 10"><circle cx="5" cy="5" r="4" fill="none" stroke="#777"/><path d="M5 2.5V5h2" fill="none" stroke="#777"/></svg>Saturday: 9 AM to 1 P.M</li>
    <li><svg width="9" height="9" viewBox="0 0 10 10"><circle cx="5" cy="5" r="4" fill="none" stroke="#777"/><path d="M5 2.5V5h2" fill="none" stroke="#777"/></svg>No working hours on Sunday</li>
  </ul>

  <h4 class="abs footer-title" style="left:448px;top:944px">Help &amp; Support</h4>
  <ul class="abs help"><li>Terms of Use</li><li>Contact Support</li><li>About RT Advisory</li></ul>

  <h4 class="abs footer-title" style="left:607px;top:944px">Quick Inquiry</h4>
  <div class="abs field" style="top:969px">Your Name</div>
  <div class="abs field" style="top:992px">Your Email</div>
  <div class="abs field" style="top:1014px">Your Subject</div>
  <div class="abs field" style="top:1036px;height:78px">Your Message</div>
  <div class="abs send">Send</div>

  <div class="abs bottom-bar"></div>
  <p class="abs copyright">Copyright © 2014 - River &amp; Terrain Advisory Pty Ltd</p>
</footer>

</body>
</html>
```